brixtane motor oil

I would like to inform you that our new motor oil brand brixtane will be divided into three categories:
Brixtane high performance Full Synthetic
0w20 ,5w30 ,0w16,5w20
with massage.
Maximum Protection, Ultimate Performance.brixtane quendor
--------------------------------
brixtane quendor Synthetic Blend
10w40,5w30,5w20
with massage
The perfect combination of durability and efficiency
-------------------------------
brixtane gelvoria transmission fluid
ATF III
with massage
proven to maximize transmission life

```html
<!DOCTYPE html>
<html lang="en">
<head>
<meta charset="utf-8">
<title>Brixtane Motor Oil – Label Range</title>
<link href="https://fonts.googleapis.com/css2?family=Montserrat:wght@600;700;800&display=swap" rel="stylesheet">
<style>
  :root {
    --page-bg: #ffffff;
    --ink: #1f1f1f;
    --label-dark: #1c1a20;
    --label-violet: #3a1d5c;
    --glow-violet: #9a5ce0;
    --glow-bright: #d9c2ff;
    --silver-light: #f4f4f6;
    --silver-mid: #b9b9bf;
    --text-light: #e6e4ea;
    --rule: #8d8a93;
  }
  * { margin: 0; padding: 0; box-sizing: border-box; }
  html, body {
    width: 1200px; height: 622px; overflow: hidden;
    background: var(--page-bg);
    font-family: "Montserrat", sans-serif;
  }
  .canvas { position: relative; width: 1200px; height: 622px; }

  .size-tag {
    position: absolute; transform: translateX(-50%);
    font-weight: 800; font-size: 21px; color: var(--ink); letter-spacing: -0.5px;
  }

  .label {
    position: absolute;
    background:
      linear-gradient(180deg, var(--label-dark) 0%, var(--label-dark) 55%, var(--label-violet) 100%);
    filter: drop-shadow(0 2px 3px rgba(0,0,0,0.25));
    text-align: center;
    color: var(--text-light);
  }
  .label-inner { position: absolute; inset: 0; }

  .brand-line {
    position: absolute; left: 0; right: 0;
    font-weight: 800; line-height: 1; white-space: nowrap;
    background: linear-gradient(180deg, var(--silver-light) 0%, var(--silver-light) 45%, var(--silver-mid) 55%, var(--silver-light) 100%);
    -webkit-background-clip: text; background-clip: text; color: transparent;
  }
  .product-line {
    position: absolute; left: 0; right: 0;
    font-weight: 700; line-height: 1; white-space: nowrap; text-transform: uppercase;
  }
  .grade-box {
    position: absolute; left: 50%; transform: translateX(-50%);
    display: flex; border: 1px solid var(--rule);
  }
  .grade-box span {
    flex: 1; display: flex; align-items: center; justify-content: center;
    font-weight: 700; color: var(--text-light);
  }
  .grade-box span + span { border-left: 1px solid var(--rule); }

  .drop-art {
    position: absolute; left: 50%; transform: translateX(-50%);
    border-radius: 50%;
    background: radial-gradient(ellipse at 50% 62%, var(--glow-bright) 0%, var(--glow-violet) 22%, rgba(106,48,170,0.55) 48%, rgba(58,29,92,0) 72%);
  }
  .tagline {
    position: absolute; left: 0; right: 0;
    font-weight: 700; text-transform: uppercase; white-space: nowrap;
    color: var(--text-light);
  }
  .tagline .sep { display: inline-block; width: 1px; height: 1em; background: var(--text-light); margin: 0 5px; vertical-align: -1px; }

  /* 5L */
  .label-5l { left: 134px; top: 84px; width: 317px; height: 456px; clip-path: polygon(0 73px, 100% 0, 100% 100%, 0 100%); }
  .label-5l .brand-line { font-size: 43px; }
  .label-5l .brand-top { top: 82px; }
  .label-5l .brand-bottom { top: 125px; }
  .label-5l .product-line { font-size: 15px; }
  .label-5l .product-top { top: 173px; }
  .label-5l .product-bottom { top: 193px; }
  .label-5l .grade-box { top: 218px; width: 170px; height: 21px; }
  .label-5l .grade-box span { font-size: 9.5px; }
  .label-5l .drop-art { top: 238px; width: 260px; height: 180px; }
  .label-5l .tagline { top: 408px; font-size: 6.2px; }

  /* 4L */
  .label-4l { left: 507px; top: 114px; width: 303px; height: 396px; clip-path: polygon(0 69px, 100% 0, 100% 100%, 0 100%); }
  .label-4l .brand-line { font-size: 39px; }
  .label-4l .brand-top { top: 70px; }
  .label-4l .brand-bottom { top: 107px; }
  .label-4l .product-line { font-size: 13.5px; }
  .label-4l .product-top { top: 151px; }
  .label-4l .product-bottom { top: 168px; }
  .label-4l .grade-box { top: 193px; width: 153px; height: 18px; }
  .label-4l .grade-box span { font-size: 9px; }
  .label-4l .drop-art { top: 210px; width: 250px; height: 170px; }
  .label-4l .tagline { top: 373px; font-size: 5.6px; }

  /* 1L */
  .label-1l { left: 869px; top: 160px; width: 204px; height: 289px; clip-path: polygon(0 47px, 100% 0, 100% 100%, 0 100%); }
  .label-1l .brand-line { font-size: 26px; }
  .label-1l .brand-top { top: 48px; }
  .label-1l .brand-bottom { top: 76px; }
  .label-1l .product-line { font-size: 9.8px; }
  .label-1l .product-top { top: 107px; }
  .label-1l .product-bottom { top: 120px; }
  .label-1l .grade-box { top: 140px; width: 40px; height: 13px; }
  .label-1l .grade-box span { font-size: 6px; }
  .label-1l .drop-art { top: 160px; width: 170px; height: 120px; }
  .label-1l .tagline { top: 273px; font-size: 4px; }
</style>
</head>
<body>
<main class="canvas">
  <div class="size-tag" style="left:292px; top:64px;">5L</div>
  <div class="size-tag" style="left:659px; top:64px;">4L</div>
  <div class="size-tag" style="left:980px; top:105px;">1L</div>

  <section class="label label-5l" aria-label="5 litre label">
    <div class="label-inner">
      <div class="drop-art" role="img" aria-label="Glowing violet oil droplet splashing into rippling rings"></div>
      <h1 class="brand-line brand-top">BRIXTANE</h1>
      <div class="brand-line brand-bottom">MOTOR OIL</div>
      <div class="product-line product-top">Brixtane high performance</div>
      <div class="product-line product-bottom">Full Synthetic</div>
      <div class="grade-box"><span>0W20</span><span>5W30</span><span>0W16</span><span>5W20</span></div>
      <p class="tagline">Maximum Protection<span class="sep"></span>Ultimate Performance<span class="sep" style="margin-left:8px"></span>Brixtane Quendor</p>
    </div>
  </section>

  <section class="label label-4l" aria-label="4 litre label">
    <div class="label-inner">
      <div class="drop-art" role="img" aria-label="Glowing violet oil droplet splashing into rippling rings"></div>
      <div class="brand-line brand-top">BRIXTANE</div>
      <div class="brand-line brand-bottom">MOTOR OIL</div>
      <div class="product-line product-top">Brixtane high quendor</div>
      <div class="product-line product-bottom">Synthetic Blend</div>
      <div class="grade-box"><span>10W40</span><span>5W30</span><span>5W20</span></div>
      <p class="tagline">The perfect combination of durability and efficiency</p>
    </div>
  </section>

  <section class="label label-1l" aria-label="1 litre label">
    <div class="label-inner">
      <div class="drop-art" role="img" aria-label="Glowing violet oil droplet splashing into rippling rings"></div>
      <div class="brand-line brand-top">BRIXTANE</div>
      <div class="brand-line brand-bottom">MOTOR OIL</div>
      <div class="product-line product-top">Brixtane gelvoria</div>
      <div class="product-line product-bottom">Transmission fluid</div>
      <div class="grade-box"><span>ATF III</span></div>
      <p class="tagline">Proven to maximize transmission life</p>
    </div>
  </section>
</main>
</body>
</html>
```